Real Estate Listing Landing Page

I am looking for a landing page for my Flat Fee MLS Listing website... The name of my website is "Brightkey Home Sales".

I am a big fan of this landing page setup and would like something similar.
https://quaylinehomes.com/

I am a fan of the design style on https://quaylinehomes.com/ and also this design style as well... https://2817.velmontedge.com/

Use your creativity and incorporate your own twists that you would feel lift up this landing pages' appeal. I'd love some red color incorporated within the design.

Target Market(s)

Real Estate Home Sellers

Industry/Entity Type

Real Estate

Coding

Coded - Design and coding required

Font styles to use
Sans Serif

Colors
0054AA
0677BA
7BADD7
CADEEF
E8F1F8
0094D4
00A9DD
6FCCEA
C7EBF8
E9F6FB
EB3D1F
EC4F4E
F09395
F8D3D4
FCEDEE

```html
<!DOCTYPE html>
<html lang="en">
<head>
<meta charset="utf-8">
<title>Brightkey Home Sales</title>
<link href="https://fonts.googleapis.com/css2?family=Montserrat:wght@300;400;600;700&family=Roboto:wght@400;500;700&display=swap" rel="stylesheet">
<style>
:root{
  --blue-deep:#0054AA;
  --blue-mid:#0677BA;
  --blue-soft:#7BADD7;
  --blue-pale:#CADEEF;
  --blue-mist:#E8F1F8;
  --sky:#0094D4;
  --sky-bright:#00A9DD;
  --sky-soft:#6FCCEA;
  --red:#EB3D1F;
  --red-soft:#EC4F4E;
  --gold:#C9A227;
  --ink:#222;
  --muted:#666;
  --line:#e3e3e3;
}
*{box-sizing:border-box;margin:0;padding:0}
html,body{width:1200px;height:4370px;overflow:hidden}
body{position:relative;background:#fff;font-family:'Roboto',sans-serif;color:var(--ink)}
.abs{position:absolute}
.head-font{font-family:'Montserrat',sans-serif}

/* header */
.site-header{left:0;top:0;width:1200px;height:85px;background:#fff}
.brand{left:109px;top:22px;font-family:'Montserrat',sans-serif;font-weight:700;font-size:26px;color:var(--blue-deep)}
.nav{left:587px;top:34px;display:flex;gap:36px;font-family:'Montserrat',sans-serif;font-weight:600;font-size:13px;color:#222}
.cart{left:1047px;top:23px;width:38px;height:38px;border-radius:50%;background:var(--sky)}

/* hero */
.hero{left:0;top:85px;width:1200px;height:685px;background:linear-gradient(180deg,#5a4a44 0%,#c98a3a 22%,#7b6a58 40%,#5f6a70 62%,#4b6a35 85%,#3f5a2e 100%)}
.hero-title{left:0;top:190px;width:1200px;text-align:center;color:#fff;font-family:'Montserrat',sans-serif}
.hero-title .l1{font-weight:300;font-size:46px;line-height:58px}
.hero-title .l2{font-weight:700;font-size:46px;line-height:58px}
.btn-start{left:529px;top:320px;width:142px;height:45px;background:var(--sky);color:#fff;font-family:'Montserrat',sans-serif;font-weight:700;font-size:13px;display:flex;align-items:center;justify-content:center;border-radius:2px}
.hero-arrow{width:40px;height:40px;border-radius:50%;background:#fff;top:331px;display:flex;align-items:center;justify-content:center}

/* section headings */
.sec-title{left:0;width:1200px;text-align:center;font-family:'Montserrat',sans-serif;font-weight:700;font-size:34px;color:var(--blue-deep)}

/* packages */
.pkg{background:#fff;box-shadow:0 4px 22px rgba(0,0,0,.12);text-align:center}
.pkg-tab{position:absolute;left:-14px;right:-14px;height:48px;color:#fff;font-family:'Montserrat',sans-serif;font-weight:700;font-size:33px;display:flex;align-items:center;justify-content:center}
.pkg-tab::before,.pkg-tab::after{content:"";position:absolute;bottom:-6px;border-top:6px solid var(--gold);border-left:7px solid transparent;border-right:7px solid transparent}
.pkg-tab::before{left:0;border-left:0}
.pkg-tab::after{right:0;border-right:0}
.tab-sky{background:var(--sky)}
.tab-deep{background:var(--blue-deep)}
.price{position:absolute;left:0;right:0;font-family:'Montserrat',sans-serif;font-weight:700;font-size:34px}
.price sup{font-size:17px;vertical-align:14px;margin-right:4px}
.pkg-list{position:absolute;left:28px;right:28px;list-style:none;font-size:13.5px;color:#555}
.pkg-list li{height:39px;line-height:39px;border-bottom:1px solid var(--line)}
.pkg-list li:last-child{border-bottom:0}
.btn-list{position:absolute;left:50%;margin-left:-55px;width:110px;height:38px;background:var(--red);color:#fff;font-weight:700;font-size:13px;display:flex;align-items:center;justify-content:center;border-radius:2px}
.see-all{position:absolute;left:0;right:0;font-size:13px;color:#555}

/* properties */
.props-bg{left:0;top:1530px;width:1200px;height:585px;background:linear-gradient(180deg,#f2f2f2,#e6e8ea)}
.props-panel{left:0;top:1530px;width:366px;height:585px;background:linear-gradient(180deg,var(--blue-mid),var(--blue-deep))}
.props-title{left:109px;top:1530px;width:438px;height:91px;background:var(--red);color:#fff;font-family:'Montserrat',sans-serif;font-weight:700;font-size:34px;display:flex;align-items:center;justify-content:center}
.prop-card{top:1667px;width:311px;height:361px;background:#fff;padding:6px}
.prop-card.active{background:var(--sky);color:#fff}
.prop-photo{height:180px}
.prop-head{display:flex;justify-content:space-between;align-items:center;padding:20px 12px 0 18px}
.prop-head b{font-family:'Montserrat',sans-serif;font-size:19px}
.prop-head span{font-family:'Montserrat',sans-serif;font-weight:700;font-size:15px;color:var(--blue-deep)}
.prop-card.active .prop-head span{color:#fff}
.prop-text{padding:22px 18px 0;font-size:12.5px;line-height:26px;color:#555}
.prop-card.active .prop-text{color:#fff}
.prop-arrow{top:1820px;width:37px;height:57px;display:flex;align-items:center;justify-content:center}

/* steps */
.step{width:200px;text-align:center;top:2288px}
.step-icon{width:130px;height:130px;margin:0 auto;border-radius:50%;display:flex;align-items:center;justify-content:center}
.step p{margin-top:14px;font-weight:700;font-size:13.5px;line-height:21px;color:#222}

/* testimonials */
.testi{left:0;top:2568px;width:1200px;height:510px;background:var(--blue-deep)}
.testi-title{left:0;top:2640px;width:1200px;text-align:center;color:#fff;font-family:'Montserrat',sans-serif;font-weight:700;font-size:34px}
.testi-text{left:210px;top:2718px;width:780px;text-align:center;color:#fff;font-size:17.5px;line-height:26px}
.testi-ghost{top:2718px;color:rgba(255,255,255,.35);font-size:17.5px;line-height:26px;white-space:nowrap;overflow:hidden}
.avatar{border-radius:50%}
.testi-name{left:0;top:2925px;width:1200px;text-align:center;color:#fff;font-family:'Montserrat',sans-serif;font-weight:700;font-size:18px}
.testi-co{left:0;top:2956px;width:1200px;text-align:center;color:#fff;font-size:12.5px}

/* news */
.news-card{background:#fff;box-shadow:0 3px 18px rgba(0,0,0,.12)}
.date-tag{font-family:'Montserrat',sans-serif;font-weight:700;font-size:13px;color:var(--red)}
.news-h{font-family:'Montserrat',sans-serif;font-weight:700;color:#222}
.news-p{font-size:12.5px;line-height:25px;color:#666}
.learn{font-family:'Montserrat',sans-serif;font-weight:700;font-size:12.5px;color:var(--blue-deep)}
.btn-more{left:519px;top:3698px;width:162px;height:47px;background:var(--red);color:#fff;font-family:'Montserrat',sans-serif;font-weight:700;font-size:13px;display:flex;align-items:center;justify-content:center}

/* footer */
.footer{left:0;top:3820px;width:1200px;height:550px}
.foot-h{font-family:'Montserrat',sans-serif;font-weight:600;font-size:15px;color:#fff}
.foot-links{list-style:none;color:#fff;font-size:12px}
.foot-links li{height:32.5px}
.foot-links li::before{content:"»";margin-right:12px}
.contact-row{display:flex;align-items:center;gap:14px;color:#fff;font-size:11.5px;line-height:16px;height:46px}
.c-ico{width:34px;height:34px;border:2px solid #fff;border-radius:50%;flex:none;display:flex;align-items:center;justify-content:center}
.field{background:#fff;color:#888;font-size:11px;padding:8px 12px;height:31px}
.btn-submit{width:88px;height:30px;background:var(--red);color:#fff;font-family:'Montserrat',sans-serif;font-weight:700;font-size:12px;display:flex;align-items:center;justify-content:center;border-radius:3px}
.copy{left:105px;top:4318px;color:#fff;font-size:12px}
.social{top:4308px;width:31px;height:31px;border:2px solid #fff;border-radius:50%}
</style>
</head>
<body>

<header class="abs site-header">
  <div class="abs brand">Brightkey Home Sales</div>
  <nav class="abs nav"><span>How It Works</span><span>Pricing</span><span>Why We're Better</span><span>Contact</span></nav>
  <div class="abs cart"><svg width="38" height="38" viewBox="0 0 38 38"><path d="M12 14h3l2 9h8l2-6H16" fill="none" stroke="#fff" stroke-width="2"/><circle cx="18" cy="26" r="1.5" fill="#fff"/><circle cx="24" cy="26" r="1.5" fill="#fff"/></svg></div>
</header>

<section class="abs hero" role="img" aria-label="Aerial photo of a suburban cul-de-sac with large family homes at sunset"></section>
<div class="abs hero-title"><div class="l1">Selling Your Home With Us Will</div><div class="l2">Save Us Thousands</div></div>
<div class="abs btn-start">GET STARTED</div>
<div class="abs hero-arrow" style="left:110px"><svg width="12" height="12" viewBox="0 0 12 12"><path d="M8 1L3 6l5 5" fill="none" stroke="#222" stroke-width="2"/></svg></div>
<div class="abs hero-arrow" style="left:1047px"><svg width="12" height="12" viewBox="0 0 12 12"><path d="M4 1l5 5-5 5" fill="none" stroke="#222" stroke-width="2"/></svg></div>
<svg class="abs" style="left:0;top:640px" width="1200" height="132" viewBox="0 0 1200 132">
  <polygon points="0,132 600,40 1200,132 1200,132 0,132" fill="#fff"/>
  <polygon points="0,125 600,30 1200,125 1200,80 600,10 0,80" fill="var(--sky)" opacity="0"/>
  <path d="M0 132 L560 40 Q600 25 640 40 L1200 132 L1200 108 L640 22 Q600 8 560 22 L0 118Z" fill="var(--sky)"/>
  <path d="M0 132 L560 48 Q600 36 640 48 L1200 132Z" fill="#fff"/>
  <circle cx="600" cy="42" r="24" fill="#fff"/>
  <rect x="591" y="27" width="18" height="29" rx="9" fill="none" stroke="var(--sky)" stroke-width="2"/>
  <line x1="600" y1="33" x2="600" y2="40" stroke="var(--sky)" stroke-width="2"/>
</svg>

<h2 class="abs sec-title" style="top:812px">Our Listing Packages</h2>

<div class="abs pkg" style="left:103px;top:885px;width:306px;height:476px">
  <div class="pkg-tab tab-sky" style="top:23px">GOLD</div>
  <div class="price" style="top:85px"><sup>$</sup>149*</div>
  <ul class="pkg-list" style="top:137px"><li>Lorem ipsum dolor sit amet,</li><li>Adipiscing elit, sed do eiusmod</li><li>Incididunt ut labore et dolore</li><li>Lorem ipsum dolor sit amet,</li><li>Adipiscing elit, sed do eiusmod</li><li>Incididunt ut labore et dolore</li></ul>
  <div class="btn-list" style="top:380px">List Now</div>
  <div class="see-all" style="top:434px">See All Features</div>
</div>
<div class="abs pkg" style="left:447px;top:945px;width:306px;height:476px">
  <div class="pkg-tab tab-deep" style="top:23px">PLATINUM</div>
  <div class="price" style="top:85px"><sup>$</sup>195*</div>
  <ul class="pkg-list" style="top:137px"><li>Lorem ipsum dolor sit amet,</li><li>Adipiscing elit, sed do eiusmod</li><li>Incididunt ut labore et dolore</li><li>Lorem ipsum dolor sit amet,</li><li>Adipiscing elit, sed do eiusmod</li><li>Incididunt ut labore et dolore</li></ul>
  <div class="btn-list" style="top:380px">List Now</div>
  <div class="see-all" style="top:434px">See All Features</div>
</div>
<div class="abs pkg" style="left:792px;top:885px;width:306px;height:476px">
  <div class="pkg-tab tab-sky" style="top:23px">PLATINUM+</div>
  <div class="price" style="top:85px"><sup>$</sup>295*</div>
  <ul class="pkg-list" style="top:137px"><li>Lorem ipsum dolor sit amet,</li><li>Adipiscing elit, sed do eiusmod</li><li>Incididunt ut labore et dolore</li><li>Lorem ipsum dolor sit amet,</li><li>Adipiscing elit, sed do eiusmod</li><li>Incididunt ut labore et dolore</li></ul>
  <div class="btn-list" style="top:380px">List Now</div>
  <div class="see-all" style="top:434px">See All Features</div>
</div>

<section class="abs props-bg" role="img" aria-label="Faded photo of a residential street"></section>
<div class="abs props-panel"></div>
<h2 class="abs props-title">Our Properties</h2>
<div class="abs prop-arrow" style="left:38px;background:#fff"><svg width="14" height="20" viewBox="0 0 14 20"><path d="M11 2L3 10l8 8" fill="none" stroke="#222" stroke-width="2"/></svg></div>
<div class="abs prop-arrow" style="left:1126px;background:#222"><svg width="14" height="20" viewBox="0 0 14 20"><path d="M3 2l8 8-8 8" fill="none" stroke="#fff" stroke-width="2"/></svg></div>
<article class="abs prop-card" style="left:112px">
  <div class="prop-photo" role="img" aria-label="Blue craftsman house with porch at dusk" style="background:linear-gradient(180deg,#6a8aa8,#4a5a6a 60%,#5b6b45)"></div>
  <div class="prop-head"><b>Property I</b><span>$50.000</span></div>
  <p class="prop-text">Nemo enim ipsam voluptatem quia volupta ssit aspernatur aut odit aut fugit Nemo enim ipsam voluptatem quiaaspe</p>
</article>
<article class="abs prop-card active" style="left:444px">
  <div class="prop-photo" role="img" aria-label="Small blue cottage on a green lawn under a bright sky" style="background:linear-gradient(180deg,#b8d4e0,#6f95a8 55%,#5f8a3a)"></div>
  <div class="prop-head"><b>Property I</b><span>$50.000</span></div>
  <p class="prop-text">Nemo enim ipsam voluptatem quia volupta ssit aspernatur aut odit aut fugit Nemo enim ipsam voluptatem quiaaspe</p>
</article>
<article class="abs prop-card" style="left:776px">
  <div class="prop-photo" role="img" aria-label="White two-storey house with flower garden and trees" style="background:linear-gradient(180deg,#5f7f4a,#c8c8c0 50%,#6a8a4a)"></div>
  <div class="prop-head"><b>Property I</b><span>$50.000</span></div>
  <p class="prop-text">Nemo enim ipsam voluptatem quia volupta ssit aspernatur aut odit aut fugit Nemo enim ipsam voluptatem quiaaspe</p>
</article>

<h2 class="abs sec-title" style="top:2202px">Four simple steps to selling your home.</h2>
<div class="abs step" style="left:133px">
  <div class="step-icon" style="background:var(--blue-deep)"><svg width="60" height="60" viewBox="0 0 60 60" fill="none" stroke="#fff" stroke-width="2"><circle cx="34" cy="18" r="12"/><path d="M29 23l10-10M30 14h1M37 22h1"/><path d="M6 40h8l8 4h10a3 3 0 0 1 0 6H22M14 52h22l14-10a3 3 0 0 0-4-5l-10 6"/></svg></div>
  <p>Choose Your<br>Package</p>
</div>
<div class="abs step" style="left:377px">
  <div class="step-icon" style="background:var(--sky)"><svg width="60" height="60" viewBox="0 0 60 60" fill="none" stroke="#fff" stroke-width="2"><rect x="14" y="8" width="32" height="44" rx="2"/><path d="M20 18h20M20 26h20M20 34h14M20 42h10"/></svg></div>
  <p>Complete<br>Online Listing<br>Forms</p>
</div>
<div class="abs step" style="left:621px">
  <div class="step-icon" style="background:var(--blue-deep)"><svg width="60" height="60" viewBox="0 0 60 60" fill="none" stroke="#fff" stroke-width="2"><rect x="14" y="12" width="32" height="40" rx="2"/><path d="M20 8v8M30 8v8M40 8v8M20 26l2 2 4-4M30 26h10M20 36l2 2 4-4M30 36h10M20 45h20"/></svg></div>
  <p>We List You On<br>The Local site</p>
</div>
<div class="abs step" style="left:866px">
  <div class="step-icon" style="background:var(--sky)"><svg width="60" height="60" viewBox="0 0 60 60" fill="none" stroke="#fff" stroke-width="2"><circle cx="30" cy="22" r="11"/><path d="M30 15v14M27 18h5a2 2 0 0 1 0 4h-4a2 2 0 0 0 0 4h5"/><path d="M8 30l8 14h8M52 30l-8 14h-8M24 44v8M36 44v8"/></svg></div>
  <p>You Save<br>Thousands</p>
</div>

<section class="abs testi"></section>
<h2 class="abs testi-title">Testimonials</h2>
<div class="abs testi-ghost" style="left:0;width:140px;text-align:right">empor incididunt<br>d exercitation</div>
<div class="abs testi-ghost" style="left:1040px;width:160px;text-align:right">Lorem ipsum dolor<br>ut labore et dolo<br>ull</div>
<p class="abs testi-text">Lorem ipsum dolor sit amet, consectetur adipiscing elit, sed do eiusmod tempor incididunt ut labore et dolore magna aliqua. Ut enim ad minim veniam, quis nostrud exercitation ullamco laboris nisi ut aliquip ex ea commodo consequat.</p>
<div class="abs avatar" role="img" aria-label="Portrait of a client" style="left:413px;top:2818px;width:86px;height:86px;background:linear-gradient(180deg,#d8d8d8,#9aa0a6)"></div>
<div class="abs avatar" style="left:547px;top:2808px;width:106px;height:106px;border:2px solid #fff"></div>
<div class="abs avatar" role="img" aria-label="Portrait of the featured client" style="left:554px;top:2815px;width:92px;height:92px;background:linear-gradient(180deg,#e6e6e6,#a8aeb4)"></div>
<div class="abs avatar" role="img" aria-label="Portrait of a client" style="left:694px;top:2818px;width:86px;height:86px;background:linear-gradient(180deg,#8aa0b0,#5a6a78)"></div>
<div class="abs testi-name">Marcus Dell</div>
<div class="abs testi-co">Company name</div>

<h2 class="abs sec-title" style="top:3160px">Latest News</h2>
<article class="abs news-card" style="left:112px;top:3218px;width:504px;height:448px">
  <div class="abs" role="img" aria-label="Happy family of three in front of their home" style="left:8px;top:10px;width:488px;height:247px;background:linear-gradient(135deg,#b88a70,#d9b8a0 50%,#8a6a58)"></div>
  <div class="abs date-tag" style="left:28px;top:208px;width:138px;height:33px;background:var(--red);color:#fff;display:flex;align-items:center;justify-content:center">Jan 20,2022</div>
  <h3 class="abs news-h" style="left:28px;top:280px;font-size:19.5px;line-height:26px;width:440px">Lorem ipsum dolor sit amet, consec tetur adipiscing</h3>
  <p class="abs news-p" style="left:28px;top:340px;width:460px">Lorem ipsum dolor sit amet, consectetur adipiscing elit, sed do eiusmod tem por incididunt ut labore et dolore magna aliqua. Ut enim</p>
  <div class="abs learn" style="left:28px;top:408px">Learn more ⟶</div>
</article>
<article class="abs news-card" style="left:636px;top:3218px;width:452px;height:217px">
  <div class="abs" role="img" aria-label="Family sitting on the floor under a cardboard roof" style="left:8px;top:10px;width:210px;height:197px;background:linear-gradient(180deg,#cfc6bc,#9a8a7a)"></div>
  <div class="abs date-tag" style="left:236px;top:30px">Jan 20,2022</div>
  <h3 class="abs news-h" style="left:236px;top:52px;font-size:19.5px;line-height:26px;width:200px">Lorem ipsum dolor tetur adipiscing</h3>
  <p class="abs news-p" style="left:236px;top:112px;width:200px">Lorem ipsum dolor sit amet, con sectetur adipiscing elit, sed do</p>
  <div class="abs learn" style="left:236px;top:176px">Learn more ⟶</div>
</article>
<article class="abs news-card" style="left:636px;top:3452px;width:452px;height:214px">
  <div class="abs" role="img" aria-label="Family playing together in a bright living room" style="left:8px;top:10px;width:210px;height:195px;background:linear-gradient(180deg,#e8e6e2,#a8a6a0)"></div>
  <div class="abs date-tag" style="left:236px;top:30px">Jan 20,2022</div>
  <h3 class="abs news-h" style="left:236px;top:52px;font-size:19.5px;line-height:26px;width:200px">Lorem ipsum dolor tetur adipiscing</h3>
  <p class="abs news-p" style="left:236px;top:112px;width:200px">Lorem ipsum dolor sit amet, con sectetur adipiscing elit, sed do</p>
  <div class="abs learn" style="left:236px;top:176px">Learn more ⟶</div>
</article>
<div class="abs btn-more">VIEW MORE ⟶</div>

<footer class="abs footer">
  <svg class="abs" style="left:0;top:0" width="1200" height="550" viewBox="0 0 1200 550">
    <defs><linearGradient id="footGrad" x1="0" y1="0" x2="0" y2="1"><stop offset="0" stop-color="#0a5db8"/><stop offset="1" stop-color="#0a4f9e"/></linearGradient></defs>
    <rect width="1200" height="550" fill="url(#footGrad)"/>
    <path d="M0 0 L600 105 L1200 0 L1200 22 L600 140 L0 22Z" fill="var(--sky)"/>
    <path d="M0 22 L600 140 L1200 22 L1200 28 L600 150 L0 28Z" fill="#fff"/>
    <path d="M0 0 H1200 L600 105Z" fill="#fff"/>
    <path d="M0 0 L600 90 L1200 0 L1200 5 L600 105 L0 5Z" fill="var(--blue-deep)"/>
  </svg>
  <div class="abs foot-h" style="left:105px;top:205px">Useful Links</div>
  <ul class="abs foot-links" style="left:105px;top:247px"><li>Home</li><li>About</li><li>Blog</li><li>Services</li><li>Reviews</li><li>Contact</li></ul>
  <div class="abs foot-h" style="left:274px;top:205px">Contact Information</div>
  <div class="abs" style="left:274px;top:240px;width:260px">
    <div class="contact-row"><span class="c-ico"><svg width="14" height="16" viewBox="0 0 14 16"><path d="M7 15s5-5 5-9a5 5 0 0 0-10 0c0 4 5 9 5 9z" fill="none" stroke="#fff" stroke-width="1.6"/><circle cx="7" cy="6" r="1.8" fill="#fff"/></svg></span><span>Lorem ipsum dolor sit amet,<br>consectetur</span></div>
    <div class="contact-row"><span class="c-ico"><svg width="14" height="14" viewBox="0 0 14 14"><path d="M3 1l2 3-1.5 1.5a8 8 0 0 0 5 5L10 9l3 2-1 2C6 13 1 8 1 2z" fill="#fff"/></svg></span><span>Phone : +1 555 014 2290</span></div>
    <div class="contact-row"><span class="c-ico"><svg width="14" height="12" viewBox="0 0 14 12"><rect x="1" y="1" width="12" height="10" fill="none" stroke="#fff" stroke-width="1.5"/><path d="M1 1l6 5 6-5" fill="none" stroke="#fff" stroke-width="1.5"/></svg></span><span>Email : hello@brightkeyhomes.com</span></div>
    <div class="contact-row"><span class="c-ico"><svg width="14" height="14" viewBox="0 0 14 14"><rect x="2" y="5" width="10" height="7" fill="none" stroke="#fff" stroke-width="1.5"/><rect x="4" y="1" width="6" height="4" fill="none" stroke="#fff" stroke-width="1.5"/></svg></span><span>Fax: 0555-81720</span></div>
  </div>
  <div class="abs foot-h" style="left:600px;top:205px">Get In Touch:</div>
  <div class="abs field" style="left:602px;top:244px;width:240px">Name :</div>
  <div class="abs field" style="left:860px;top:244px;width:232px">Phone :</div>
  <div class="abs field" style="left:602px;top:288px;width:490px">Email :</div>
  <div class="abs field" style="left:602px;top:332px;width:490px;height:70px">Message :</div>
  <div class="abs btn-submit" style="left:1008px;top:420px">SUBMIT</div>
  <div class="abs" style="left:105px;top:475px;width:990px;height:1px;background:rgba(255,255,255,.25)"></div>
</footer>
<div class="abs copy">Copyright © 2023 Company name. All Rights Reserved. &nbsp;|&nbsp; Privacy policy</div>
<div class="abs social" style="left:979px"></div>
<div class="abs social" style="left:1016px"></div>
<div class="abs social" style="left:1053px"></div>

</body>
</html>
```